Slick Facebook Ad

We've recently re-branded our business to reflect our ethos "Wealth is about more than money - it's about choice." We aim to protect your hard-earned success and help achieve your lifestyle aspirations, whether that's retiring at fifty to go globetrotting, or buying your first home. We're a financial consultancy that primarily services high-net-worth clients.

Our brand is minimalist, modern (check out our website) and the brief focuses on our strong investment return for the past 12 years.

Task: The attached brief is for a Facebook advertisement. Please see competitor images as a guide to how 'returns' and 'branding' can both be displayed in a design.

Target Market(s)

+30

Font styles to use
Sans Serif

Requirements
Must have
• Creative should feature the strong investment return, and design aesthetic should be 'on-brand' (modern, minimalist, lifestyle focused).

```html
<!DOCTYPE html>
<html lang="en">
<head>
<meta charset="utf-8">
<title>Larchfield – Returns Ad Variants</title>
<link href="https://fonts.googleapis.com/css2?family=Montserrat:wght@400;500;700&display=swap" rel="stylesheet">
<style>
  :root {
    --stage: #000000;
    --brand-green: #b0bd1e;
    --ink: #3a3a3a;
    --white: #ffffff;
    --slate: #3b423f;
    --slate-deep: #2d3330;
    --leaf-light: #c9dc4a;
    --leaf-mid: #7fa22a;
    --leaf-deep: #3f6418;
  }
  * { box-sizing: border-box; margin: 0; padding: 0; }
  html, body {
    width: 1200px; height: 645px; overflow: hidden;
    background: var(--stage);
    font-family: "Montserrat", Arial, sans-serif;
  }
  .stage { position: relative; width: 1200px; height: 645px; }
  .ad {
    position: absolute; top: 74px;
    width: 506px; height: 505px; overflow: hidden;
  }
  .ad--green { left: 69px; }
  .ad--slate { left: 623px; }

  .ad__backdrop { position: absolute; inset: 0; }
  .ad--green .ad__backdrop {
    background:
      radial-gradient(circle at 78% 22%, var(--leaf-light) 0%, transparent 42%),
      radial-gradient(circle at 18% 62%, var(--leaf-deep) 0%, transparent 50%),
      linear-gradient(135deg, var(--leaf-mid) 0%, #9cbb2a 50%, #5e8420 100%);
  }
  .ad--slate .ad__backdrop {
    background: radial-gradient(circle at 70% 35%, #4a524e 0%, var(--slate) 45%, var(--slate-deep) 100%);
  }

  .ad__photo {
    position: absolute; left: 0; top: 170px; width: 440px; height: 335px;
    background:
      radial-gradient(ellipse 90px 140px at 62% 42%, rgba(235,235,230,0.38) 0%, rgba(235,235,230,0) 100%),
      radial-gradient(ellipse 170px 110px at 20% 85%, rgba(150,150,150,0.45) 0%, rgba(150,150,150,0) 100%);
  }

  .headline {
    position: absolute; left: 28px; top: 28px; color: var(--white);
  }
  .headline__intro { font-size: 15px; font-weight: 400; }
  .headline__main {
    font-size: 37px; font-weight: 400; line-height: 42px;
    letter-spacing: 0.6px; margin-top: 2px;
  }
  .headline__figure { font-weight: 700; }
  .ad--slate .headline__figure { color: var(--brand-green); }
  .headline__period { font-size: 15px; font-weight: 400; margin-top: 6px; }

  .footer-band {
    position: absolute; left: 0; bottom: 0; width: 340px; height: 41px;
    background: var(--brand-green);
    display: flex; align-items: center; gap: 11px; padding-left: 22px;
  }
  .footer-band__url { font-size: 14.5px; font-weight: 700; color: var(--ink); letter-spacing: 0.2px; }
  .footer-band__icon { width: 17px; height: 17px; }

  .corner-sweep { position: absolute; inset: 0; width: 506px; height: 505px; }

  .brand-lockup {
    position: absolute; left: 356px; top: 382px; width: 144px;
    display: flex; flex-direction: column; align-items: center;
  }
  .brand-lockup__dot {
    width: 62px; height: 62px; border-radius: 50%;
    background: var(--brand-green); margin-bottom: 16px;
  }
  .brand-lockup__name { font-size: 21px; font-weight: 500; color: var(--ink); letter-spacing: -0.3px; }
</style>
</head>
<body>
<main class="stage">

  <section class="ad ad--green">
    <div class="ad__backdrop" role="img" aria-label="Soft-focus green foliage background"></div>
    <div class="ad__photo" role="img" aria-label="Hand holding a smartphone showing a growth rate chart with a rising arrow"></div>
    <div class="headline">
      <p class="headline__intro">Our global investment portfolio</p>
      <h1 class="headline__main">DELIVERED<br><span class="headline__figure">20.5%</span> RETURNS</h1>
      <p class="headline__period">over the past 12 months.</p>
    </div>
    <svg class="corner-sweep" viewBox="0 0 506 505" aria-hidden="true">
      <path d="M298 505 C330 400 420 345 506 338 L506 505 Z" fill="#ffffff"/>
    </svg>
    <div class="footer-band">
      <svg class="footer-band__icon" viewBox="0 0 20 20" aria-hidden="true">
        <circle cx="10" cy="10" r="9" fill="#3a3a3a"/>
        <g fill="none" stroke="#b0bd1e" stroke-width="1.2">
          <ellipse cx="10" cy="10" rx="4" ry="9"/>
          <line x1="1" y1="10" x2="19" y2="10"/>
          <line x1="2.5" y1="5.5" x2="17.5" y2="5.5"/>
          <line x1="2.5" y1="14.5" x2="17.5" y2="14.5"/>
        </g>
      </svg>
      <span class="footer-band__url">www.larchfieldhg.com</span>
    </div>
    <div class="brand-lockup">
      <div class="brand-lockup__dot"></div>
      <p class="brand-lockup__name">larchfield</p>
    </div>
  </section>

  <section class="ad ad--slate">
    <div class="ad__backdrop" role="img" aria-label="Dark slate background"></div>
    <div class="ad__photo" role="img" aria-label="Hand holding a smartphone showing a growth rate chart with a rising arrow"></div>
    <div class="headline">
      <p class="headline__intro">Our global investment portfolio</p>
      <h1 class="headline__main">DELIVERED<br><span class="headline__figure">20.5%</span> RETURNS</h1>
      <p class="headline__period">over the past 12 months.</p>
    </div>
    <svg class="corner-sweep" viewBox="0 0 506 505" aria-hidden="true">
      <path d="M298 505 C330 400 420 345 506 338 L506 505 Z" fill="#ffffff"/>
    </svg>
    <div class="footer-band">
      <svg class="footer-band__icon" viewBox="0 0 20 20" aria-hidden="true">
        <circle cx="10" cy="10" r="9" fill="#3a3a3a"/>
        <g fill="none" stroke="#b0bd1e" stroke-width="1.2">
          <ellipse cx="10" cy="10" rx="4" ry="9"/>
          <line x1="1" y1="10" x2="19" y2="10"/>
          <line x1="2.5" y1="5.5" x2="17.5" y2="5.5"/>
          <line x1="2.5" y1="14.5" x2="17.5" y2="14.5"/>
        </g>
      </svg>
      <span class="footer-band__url">www.larchfieldhg.com</span>
    </div>
    <div class="brand-lockup">
      <div class="brand-lockup__dot"></div>
      <p class="brand-lockup__name">larchfield</p>
    </div>
  </section>

</main>
</body>
</html>
```